luxury contemporary fashion website needs simple, elegant flowchart to describe the buying and selli

* Luxury, resale, preloved items are sold on this online platform
*Horizontal, simple, flowchart with 5 steps in 'friendly' font with a simple emoticon/ picture for each step
*To be positioned in the 'How we work' tab of the webpage to explain in a very simple manner the buying and selling process for the customers.
*Attached is a very rudimentary mock-up of what we would like included and an idea of a project similar to what we desire
* to confirm the text for each step, we have also attached a word file below

Industry/Entity Type

Fashion

Font styles to use
Sans Serif

Colors
86cfc6
cfeae6

Requirements
Must have
• Simple drawing / shape after each point In the closest to 'duck egg blue' fill colour you can find with a black outline

```html
<!DOCTYPE html>
<html lang="en">
<head>
<meta charset="utf-8">
<title>Bespoke Personal Concierge</title>
<link href="https://fonts.googleapis.com/css2?family=Jost:wght@300;400;600;700&display=swap" rel="stylesheet">
<style>
  :root {
    --teal: #86cfc6;
    --teal-soft: #cfeae6;
    --ink: #111111;
    --paper: #ffffff;
  }
  * { margin: 0; padding: 0; box-sizing: border-box; }
  html, body { width: 1200px; height: 300px; overflow: hidden; background: var(--paper); }
  .flow {
    position: relative; width: 1200px; height: 300px;
    font-family: "Jost", "Century Gothic", sans-serif; color: var(--ink);
  }
  .flow-title {
    position: absolute; left: 0; top: 12px; width: 100%;
    text-align: center; font-weight: 300; font-size: 37px; color: var(--teal);
    letter-spacing: 0.3px;
  }
  .flow-rule {
    position: absolute; left: 80px; top: 58px; width: 1086px; height: 1px;
    background: var(--teal-soft);
  }
  .step { position: absolute; }
  .step-heading { font-weight: 600; font-size: 17.5px; line-height: 22px; }
  .step-text { font-weight: 400; line-height: 21px; margin-top: 18px; }
  .accent { color: var(--teal); }
  .step-number {
    position: absolute; top: 252px; font-weight: 600; font-size: 31px; color: var(--teal);
  }
  .icon { display: inline-block; vertical-align: middle; }
  .payment-cloud { position: absolute; left: 716px; top: 126px; }
  .payment-label {
    position: absolute; left: 722px; top: 170px; width: 140px; text-align: center;
    font-weight: 700; font-size: 17px; color: var(--teal);
  }
  .payment-arrows { position: absolute; left: 893px; top: 128px; }
  .outcome { position: absolute; left: 977px; font-size: 16.5px; line-height: 21px; }
  .currency { position: absolute; left: 1104px; top: 114px; color: var(--teal); font-weight: 600; font-size: 12px; }
</style>
</head>
<body>
<main class="flow">
  <h1 class="flow-title">Bespoke Personal Concierge</h1>
  <div class="flow-rule"></div>

  <section class="step" style="left:81px; top:92px;">
    <h2 class="step-heading">Have items<br>&nbsp;&nbsp;&nbsp;to sell <span class="accent">?</span></h2>
    <p class="step-text" style="font-size:16.5px; margin-left:4px; line-height:22px;">
      - brand spanking<br>&nbsp;&nbsp;&nbsp;or nearly<br>&nbsp;&nbsp;&nbsp;new
      <svg class="icon" width="12" height="12" viewBox="0 0 12 12" aria-hidden="true"><circle cx="3" cy="8" r="1.3" fill="#86cfc6"/><circle cx="8" cy="3" r="1.3" fill="#86cfc6"/><circle cx="9" cy="9" r="1" fill="#86cfc6"/></svg>
    </p>
  </section>

  <section class="step" style="left:247px; top:92px;">
    <h2 class="step-heading">Personal<br>collection</h2>
    <p class="step-text" style="font-size:14px; margin-left:-5px; line-height:20px;">
      - we choose the<br>&nbsp;&nbsp;&nbsp;pieces we know<br>&nbsp;&nbsp;&nbsp;the velora<br>&nbsp;&nbsp;&nbsp;customers<br>&nbsp;&nbsp;&nbsp;will love
      <svg class="icon" width="16" height="14" viewBox="0 0 16 14" aria-hidden="true"><path d="M8 13 L1.5 6.5 A3.6 3.6 0 0 1 8 2.5 A3.6 3.6 0 0 1 14.5 6.5 Z" fill="#86cfc6"/></svg>
    </p>
  </section>

  <section class="step" style="left:396px; top:92px;">
    <h2 class="step-heading">We Prepare</h2>
    <p class="step-text" style="font-size:13px; margin-left:-10px; margin-top:34px; line-height:19px;">
      - your item for sale<br>&nbsp;&nbsp;with thorough autheticity<br>&nbsp;&nbsp;&amp; condition checks...<br>&nbsp;&nbsp;&nbsp;&nbsp;&nbsp;&nbsp;so&nbsp; you<br>&nbsp;&nbsp;&nbsp;&nbsp;&nbsp;&nbsp;don't have to !&nbsp;
      <svg class="icon" width="14" height="14" viewBox="0 0 14 14" aria-hidden="true"><circle cx="7" cy="7" r="6.5" fill="#86cfc6"/></svg>
    </p>
  </section>

  <section class="step" style="left:562px; top:92px;">
    <h2 class="step-heading">Once sold</h2>
    <p class="step-text" style="font-size:13px; margin-left:2px; margin-top:36px; line-height:19px;">
      -we lovingly<br>&nbsp;&nbsp;&nbsp;prepare the item<br><br>&nbsp;&nbsp;&nbsp;- shipped via<br>&nbsp;&nbsp;&nbsp;&nbsp;&nbsp;&nbsp;&nbsp;tracked services
      <svg class="icon" width="22" height="14" viewBox="0 0 22 14" aria-hidden="true"><path d="M1 9 L20 3 L13 12 L10 9 Z" fill="#cfeae6" stroke="#86cfc6" stroke-width="1"/></svg>
    </p>
  </section>

  <svg class="payment-cloud" width="152" height="112" viewBox="0 0 152 112" aria-hidden="true">
    <path d="M30 92 A22 22 0 0 1 24 50 A28 28 0 0 1 70 26 A26 26 0 0 1 116 36 A22 22 0 0 1 128 80 A20 20 0 0 1 100 96 A25 25 0 0 1 60 100 A20 20 0 0 1 30 92 Z"
      fill="none" stroke="#86cfc6" stroke-width="3.5" stroke-linejoin="round"/>
  </svg>
  <div class="payment-label">Your payment</div>

  <svg class="payment-arrows" width="70" height="100" viewBox="0 0 70 100" aria-hidden="true">
    <g fill="none" stroke="#86cfc6" stroke-width="3.5" stroke-linecap="round">
      <path d="M6 44 Q24 20 60 14"/>
      <path d="M52 8 L61 14 L53 21"/>
      <path d="M6 64 Q24 88 60 92"/>
      <path d="M53 85 L61 92 L52 98"/>
    </g>
  </svg>

  <div class="currency">£<sub style="font-size:9px">$</sub>€</div>
  <p class="outcome" style="top:130px;">Pocket the cash</p>
  <p class="outcome" style="top:210px;">Donate to charity<br>(full or partial amount)</p>
  <svg class="icon" style="position:absolute; left:1148px; top:222px;" width="16" height="16" viewBox="0 0 16 16" aria-hidden="true"><circle cx="8" cy="8" r="6.5" fill="none" stroke="#86cfc6" stroke-width="1.3"/></svg>

  <span class="step-number" style="left:120px;">1</span>
  <span class="step-number" style="left:272px;">2</span>
  <span class="step-number" style="left:430px;">3</span>
  <span class="step-number" style="left:595px;">4</span>
  <span class="step-number" style="left:791px;">5</span>
</main>
</body>
</html>
```